Detail Shop Business card design

i need a business card design for my new detailing company called 'Brenner's Detail Shop'. i want an all black and white design . simple, direct and to the point. i want the designer to choose a fitting font to match the logothe front should have logo, address, phone and email and the back side should have a slogan and text indicating that we offer services on anything including cars, trucks, motorcycles and RVs. slogan will read "we take pride in your ride"
maybe also very small on the back side the IG icon with Brenners_Detail_Shop

phone 482.615.7734
address 7384 E Harlow Ave
Spokane WA 99342
email: BrennersDetail@quorvail.com

Target Market(s)

all ages , auto enthusiasts

Industry/Entity Type

Automotive

Contact Information for Business Card

the front should have logo, address, phone and email and the back side should have a slogan and text indicating that we offer services on anything including cars, trucks, motorcycles and RVs. slogan will read "we take pride in your ride"

phone 482.615.7734
address 7384 E Harlow Ave
Spokane WA 99342

Colors
000000
ffffff

Requirements
Must have
• bold font and very simple design with good spacing
Nice to have
• anything creative from the designer indicating we service any types of vehicles
Should not have
• any colors ,

```html
<!DOCTYPE html>
<html lang="en">
<head>
<meta charset="utf-8">
<title>Brenner's Detail Shop – Business Card</title>
<link href="https://fonts.googleapis.com/css2?family=Alfa+Slab+One&family=Noto+Serif:ital,wght@0,400;1,400&display=swap" rel="stylesheet">
<style>
  :root {
    --ink: #000000;
    --paper: #ffffff;
    --card-black: #111111;
    --stage: #1c1c1c;
  }
  * { box-sizing: border-box; margin: 0; padding: 0; }
  html, body {
    width: 1200px; height: 1200px; overflow: hidden;
    background: var(--stage);
  }
  .canvas {
    width: 1200px; height: 1200px;
    display: flex; flex-direction: column;
    align-items: center; justify-content: center; gap: 48px;
  }
  .card {
    width: 920px; height: 526px;
    border-radius: 22px;
    position: relative; overflow: hidden;
    background: var(--card-black);
    color: var(--paper);
  }

  /* Back side */
  .card-back .services {
    position: absolute; top: 170px; left: 0; right: 0;
    text-align: center;
    font-family: "Alfa Slab One", serif;
    font-size: 29px; letter-spacing: 2px;
  }
  .card-back .services .dot { margin: 0 14px; }
  .card-back .slogan {
    position: absolute; top: 240px; left: 0; right: 0;
    text-align: center;
    font-family: "Noto Serif", serif; font-style: italic;
    font-size: 28px;
  }
  .card-back .social {
    position: absolute; top: 318px; left: 100px; right: 100px;
    display: flex; align-items: center; gap: 14px;
  }
  .card-back .rule { flex: 1; height: 1px; background: var(--paper); }
  .card-back .handle {
    display: flex; flex-direction: column; align-items: center; gap: 8px;
    font-family: "Noto Serif", serif; font-size: 21px;
    padding-top: 30px;
  }
  .card-back .handle-mark {
    width: 26px; height: 26px; background: var(--paper); border-radius: 4px;
  }

  /* Front side */
  .card-front .logo-panel {
    position: absolute; left: 0; top: 0; bottom: 0; width: 405px;
    background: var(--paper); color: var(--ink);
    display: flex; align-items: center; justify-content: center;
  }
  .card-front .brand {
    display: flex; align-items: center; gap: 16px;
    font-family: "Alfa Slab One", serif;
    font-size: 34px; line-height: 1.15; text-align: left;
  }
  .card-front .brand-dot {
    width: 22px; height: 22px; border-radius: 50%; background: var(--ink); flex: none;
  }
  .card-front .divider {
    position: absolute; left: 421px; top: 0; bottom: 0; width: 6px;
    background: var(--paper);
  }
  .card-front .contacts {
    position: absolute; left: 384px; top: 160px;
    list-style: none;
    display: flex; flex-direction: column; gap: 22px;
  }
  .card-front .contact {
    display: flex; align-items: center; gap: 26px;
    font-family: "Noto Serif", serif; font-size: 23px; letter-spacing: 0.5px;
  }
  .card-front .icon {
    width: 80px; height: 80px; border-radius: 50%;
    background: var(--ink); border: 5px solid var(--paper);
    display: flex; align-items: center; justify-content: center; flex: none;
  }
  .card-front .icon svg { width: 34px; height: 34px; }
</style>
</head>
<body>
<main class="canvas">

  <section class="card card-back" aria-label="Back of card">
    <p class="services">CARS<span class="dot">•</span>TRUCKS<span class="dot">•</span>MOTORCYCLES<span class="dot">•</span>BOATS<span class="dot">•</span>RVS</p>
    <p class="slogan">we take pride in your ride</p>
    <div class="social">
      <span class="rule"></span>
      <div class="handle">
        <span class="handle-mark"></span>
        <span>Brenners detail shop</span>
      </div>
      <span class="rule"></span>
    </div>
  </section>

  <section class="card card-front" aria-label="Front of card">
    <div class="logo-panel">
      <div class="brand">
        <span class="brand-dot"></span>
        <span>Brenner's<br>Detail Shop</span>
      </div>
    </div>
    <div class="divider"></div>
    <ul class="contacts">
      <li class="contact">
        <span class="icon">
          <svg viewBox="0 0 24 24" fill="#ffffff"><path d="M6.6 10.8c1.4 2.8 3.8 5.1 6.6 6.6l2.2-2.2c.3-.3.7-.4 1-.2 1.1.4 2.3.6 3.6.6.6 0 1 .4 1 1V20c0 .6-.4 1-1 1C10.6 21 3 13.4 3 4c0-.6.4-1 1-1h3.5c.6 0 1 .4 1 1 0 1.3.2 2.5.6 3.6.1.3 0 .7-.2 1z"/></svg>
        </span>
        <span>482.615.7734</span>
      </li>
      <li class="contact">
        <span class="icon">
          <svg viewBox="0 0 24 24" fill="none" stroke="#ffffff" stroke-width="1.8"><rect x="3" y="5.5" width="18" height="13" rx="1"/><path d="M3 6l9 7 9-7M3 18l7-6M21 18l-7-6"/></svg>
        </span>
        <span>BrennersDetail@quorvail.com</span>
      </li>
      <li class="contact">
        <span class="icon">
          <svg viewBox="0 0 24 24" fill="#ffffff"><path d="M12 2a7 7 0 0 0-7 7c0 5.2 7 13 7 13s7-7.8 7-13a7 7 0 0 0-7-7zm0 9.5A2.5 2.5 0 1 1 12 6.5a2.5 2.5 0 0 1 0 5z"/></svg>
        </span>
        <span>7384 E Harlow Ave, Spokane WA 99342</span>
      </li>
    </ul>
  </section>

</main>
</body>
</html>
```